Brightmere Business Card Redesign & Logo Update

We need to update our business cards to something more modern and fresh. Brightmere can provide the current color schemes and old design examples, but welcome creativity in helping us with this redesign. PLEASE NOTE that we no longer utilize the "tree" and/or "leaf" imagery in our branding. If able would apprecaite an update on the quality of our "words only" logo in Ai. / PNG formats too.

Target Market(s)

Investors, landowners, corporate partners, contractors

Industry/Entity Type

Environmental Restoration & Conservation

Contact Information for Business Card

Logo, persons name, title, mailing address, phone and email, website url

Font styles to use
Other font styles liked:
• Merriweather

Requirements
Nice to have
• Logo, persons name, title, mailing address, phone and email, website url, but open to ideams
Should not have
• No all back backgrounds

```html
<!DOCTYPE html>
<html lang="en">
<head>
<meta charset="utf-8">
<title>Brightmere Business Card</title>
<link rel="stylesheet" href="https://fonts.googleapis.com/css2?family=Montserrat:wght@400;600;800&display=swap">
<style>
  :root {
    --page-bg: #d6d6d4;
    --card-bg: #1f1f1f;
    --brand-orange: #f07c1e;
    --brand-green: #128a3e;
    --text-light: #f2f2f2;
    --text-muted: #d4d4d4;
  }
  html, body {
    margin: 0;
    padding: 0;
    width: 1200px;
    height: 900px;
    overflow: hidden;
    background: var(--page-bg);
    font-family: "Montserrat", Arial, sans-serif;
  }
  .canvas {
    width: 1200px;
    height: 900px;
    display: flex;
    align-items: center;
    justify-content: center;
  }
  .business-card {
    position: relative;
    width: 1000px;
    height: 571px;
    background: var(--card-bg);
    border-radius: 34px;
    color: var(--text-light);
  }
  .brand {
    position: absolute;
    left: 450px;
    top: 120px;
    text-align: left;
  }
  .brand-name {
    font-weight: 800;
    font-size: 74px;
    line-height: 1;
    letter-spacing: 1px;
    color: var(--brand-orange);
    margin: 0;
  }
  .brand-tagline {
    margin: 10px 0 0 4px;
    font-weight: 600;
    font-size: 19px;
    letter-spacing: 2.5px;
    text-transform: uppercase;
    color: var(--text-light);
  }
  .person {
    position: absolute;
    right: 570px;
    top: 292px;
    text-align: right;
  }
  .person-name {
    margin: 0;
    font-weight: 800;
    font-size: 30px;
    letter-spacing: 2px;
    text-transform: uppercase;
  }
  .person-name .given { color: var(--brand-green); }
  .person-name .family { color: var(--brand-orange); }
  .person-title {
    margin: 4px 0 0;
    font-weight: 400;
    font-size: 21px;
    letter-spacing: 1px;
    color: var(--text-muted);
  }
  .divider {
    position: absolute;
    left: 458px;
    top: 285px;
    width: 1.5px;
    height: 100px;
    background: var(--brand-green);
  }
  .contact-list {
    position: absolute;
    left: 488px;
    top: 288px;
    margin: 0;
    padding: 0;
    list-style: none;
  }
  .contact-list li {
    display: flex;
    align-items: center;
    gap: 10px;
    font-size: 21px;
    letter-spacing: 0.8px;
    line-height: 32px;
    color: var(--text-light);
  }
  .contact-icon {
    width: 17px;
    height: 17px;
    flex: none;
  }
  .address {
    position: absolute;
    left: 170px;
    top: 420px;
    margin: 0;
    font-style: normal;
    font-size: 22px;
    letter-spacing: 1px;
    color: var(--text-light);
  }
</style>
</head>
<body>
<main class="canvas">
  <section class="business-card" aria-label="Brightmere business card">
    <header class="brand">
      <h1 class="brand-name">BRIGHTMERE</h1>
      <p class="brand-tagline">Environmental Credit Company</p>
    </header>

    <div class="person">
      <h2 class="person-name"><span class="given">Dana</span> <span class="family">Whitfield</span></h2>
      <p class="person-title">CEO/Founder</p>
    </div>

    <div class="divider" aria-hidden="true"></div>

    <ul class="contact-list">
      <li>
        <svg class="contact-icon" viewBox="0 0 24 24" aria-hidden="true">
          <path fill="#f07c1e" d="M6.6 10.8a15.1 15.1 0 0 0 6.6 6.6l2.2-2.2a1 1 0 0 1 1-.25 11.4 11.4 0 0 0 3.6.57 1 1 0 0 1 1 1V20a1 1 0 0 1-1 1A17 17 0 0 1 3 4a1 1 0 0 1 1-1h3.5a1 1 0 0 1 1 1c0 1.25.2 2.45.57 3.57a1 1 0 0 1-.25 1z"/>
        </svg>
        (555) 318 2046
      </li>
      <li>
        <svg class="contact-icon" viewBox="0 0 24 24" aria-hidden="true">
          <rect x="2" y="5" width="20" height="14" rx="1.5" fill="#f07c1e"/>
          <path d="M3 6.5l9 6.5 9-6.5" fill="none" stroke="#1f1f1f" stroke-width="1.8"/>
        </svg>
        Dana@brightmere.com
      </li>
      <li>
        <svg class="contact-icon" viewBox="0 0 24 24" aria-hidden="true">
          <circle cx="12" cy="12" r="10" fill="#f07c1e"/>
          <ellipse cx="12" cy="12" rx="4.5" ry="10" fill="none" stroke="#1f1f1f" stroke-width="1.6"/>
          <path d="M2 12h20" stroke="#1f1f1f" stroke-width="1.6"/>
        </svg>
        www.brightmere.com
      </li>
    </ul>

    <address class="address">48 Alder Mill Road Country Name, AB 60931</address>
  </section>
</main>
</body>
</html>
```